Bracken Project Services - Flyer

I need a single page A4 Capability Statement, which will be used to market our services to prospective clients, both in print and via email PDF.
It needs to look professional and should incorporate the elements I have uploaded into files, these include:
Capability Statement Text
Bracken Services Company Logo
Additional Logo’s (Tools We Use)
Frame Cellar Pics can be cut into the page
I have included examples of capability statements as a guide to what i am looking for.
Regards
Derek
Engineering Consulting

```html
<!DOCTYPE html>
<html lang="en">
<head>
<meta charset="utf-8">
<title>Bracken Project Services – Capability Statement</title>
<link href="https://fonts.googleapis.com/css2?family=Roboto:wght@300;400;500&display=swap" rel="stylesheet">
<style>
:root{
  --page-bg:#d6d6d6;
  --paper:#ffffff;
  --brand-blue:#0a4fa3;
  --deep-blue:#123f8c;
  --sky:#8ecae6;
  --panel:#f2f2f3;
  --panel-dark:#e2e3e5;
  --text:#555a60;
  --ink:#222427;
}
*{margin:0;padding:0;box-sizing:border-box}
html,body{width:1041px;height:1200px;overflow:hidden;background:var(--page-bg);font-family:'Roboto',sans-serif}
.flyer{position:absolute;left:96px;top:0;width:766px;height:1082px;background:var(--paper);transform:scale(1.1091);transform-origin:0 0;overflow:hidden;color:var(--text)}
.abs{position:absolute}
.brand{left:0;top:0;width:380px;height:168px;display:flex;flex-direction:column;align-items:center;padding-top:24px}
.brand-dot{width:60px;height:60px;border-radius:50%;background:var(--brand-blue)}
.brand-name{margin-top:22px;font-size:17px;font-weight:400;letter-spacing:2px;color:var(--ink);text-align:center;line-height:1.25;text-transform:uppercase}
.hero{left:0;top:127px;width:766px;height:301px;background:linear-gradient(120deg,#eef3f8 0%,#d9e4ef 40%,#c7d6e6 70%,#e9eef4 100%)}
.hero-cut{left:0;top:0;width:766px;height:170px}
.about{left:17px;top:428px;width:365px;height:192px;background:var(--panel);padding:20px 20px 0 28px}
.team{left:17px;top:620px;width:365px;height:102px;background:var(--panel-dark);padding:12px 24px 0 22px}
.expertise{left:17px;top:722px;width:365px;height:360px;background:var(--panel);padding:14px 27px 0 22px}
h2{font-size:15.5px;font-weight:500;color:var(--deep-blue);margin-bottom:4px}
p{font-size:14px;font-weight:300;line-height:17px;text-align:justify;color:var(--text)}
.expertise p{line-height:16.6px;margin-bottom:16px}
.team p{line-height:18.5px;text-align:left}
.about p{line-height:18.5px}
.core-head{left:382px;top:428px;width:384px;height:47px;background:var(--panel-dark);padding:12px 0 0 58px;font-size:18px;font-weight:500;color:var(--deep-blue)}
.service{left:392px;width:374px}
.service .icon{position:absolute;left:0;top:-10px;width:40px;height:40px}
.service h3{margin-left:49px;font-size:15px;font-weight:500;color:var(--deep-blue)}
.service ul{list-style:none;margin:4px 0 0 49px}
.service li{font-size:14.5px;font-weight:300;line-height:18.6px;color:var(--text);padding-left:17px;position:relative}
.service li::before{content:"";position:absolute;left:1px;top:7px;width:5px;height:5px;background:#666}
.sky-bar{left:382px;top:954px;width:49px;height:128px;background:var(--sky)}
.contact{left:450px;display:flex;align-items:center;gap:11px;font-size:19px;font-weight:500;color:#444}
.contact svg{width:28px;height:28px}
</style>
</head>
<body>
<div class="flyer">
  <div class="abs hero" role="img" aria-label="Photo of colleagues reviewing documents and charts at a desk"></div>
  <svg class="abs hero-cut" viewBox="0 0 766 170" width="766" height="170">
    <polygon points="380,117 766,117 766,127 370,127" fill="#0a4fa3"/>
    <polygon points="0,127 370,127 312,168 0,168" fill="#ffffff"/>
  </svg>
  <div class="abs brand">
    <div class="brand-dot"></div>
    <div class="brand-name">Bracken Project<br>Services</div>
  </div>

  <section class="abs about">
    <h2>About Us:</h2>
    <p>Our goal is to make successful project delivery more achievable and repeatable. We are continually innovating, evolving and learning, utilizing the latest industry tools and techniques to deliver real value to our clients. We are passionate about empowering organisations to achieve their objectives, on time and on budget.</p>
  </section>
  <section class="abs team">
    <h2>Our Team</h2>
    <p>We use highly experienced industry professionals who engage with our clients to deliver practical and innovative project control solutions.</p>
  </section>
  <section class="abs expertise">
    <h2 style="margin-bottom:8px">Our Expertise</h2>
    <p>For over 20 years we have been helping our clients to successfully deliver capital projects within the pharmaceutical and biotechnology sectors.</p>
    <p>During this time, we have worked closely with multinational healthcare companies and leading A&amp;E firms, on a variety of business-critical projects.</p>
    <p>Our experience and knowledge of project control gives our client’s unparalleled visibility of Cost, Schedule and Risk through the lifecycle of their projects.</p>
    <p>This visibility allows our clients to make timely informed decisions which increase efficiency and project performance.</p>
  </section>

  <div class="abs core-head">Core Services:</div>

  <section class="abs service" style="top:500px">
    <svg class="icon" viewBox="0 0 40 40"><circle cx="20" cy="20" r="19" fill="#0a4fa3"/><rect x="11" y="12" width="16" height="15" rx="1.5" fill="none" stroke="#fff" stroke-width="1.6"/><line x1="11" y1="16.5" x2="27" y2="16.5" stroke="#fff" stroke-width="1.6"/><g fill="#fff"><rect x="13.5" y="19" width="2.5" height="2.5"/><rect x="17.5" y="19" width="2.5" height="2.5"/><rect x="21.5" y="19" width="2.5" height="2.5"/><rect x="13.5" y="23" width="2.5" height="2.5"/></g><circle cx="27" cy="27" r="4.5" fill="#0a4fa3" stroke="#fff" stroke-width="1.4"/></svg>
    <h3>Planning and Scheduling</h3>
    <ul><li>Tender Planning</li><li>Interactive Planning / Pull Planning</li><li>CPM Planning &amp; Scheduling</li><li>Agile / Lean Planning Methodology</li><li>Independent Schedule Quality Assessment</li><li>Schedule Risk Analysis (Monte Carlo)</li><li>Training</li></ul>
  </section>

  <section class="abs service" style="top:667px">
    <svg class="icon" viewBox="0 0 40 40"><circle cx="20" cy="20" r="19" fill="#0a4fa3"/><g fill="#fff"><circle cx="20" cy="14" r="3.2"/><path d="M14 25a6 6 0 0 1 12 0z"/><circle cx="12" cy="18" r="2.5"/><path d="M7.5 27a4.5 4.5 0 0 1 9 0z"/><circle cx="28" cy="18" r="2.5"/><path d="M23.5 27a4.5 4.5 0 0 1 9 0z"/></g></svg>
    <h3>Management of Risk</h3>
    <ul><li>Risk Management Policies &amp; Procedures</li><li>Risk Management Strategy</li><li>Risk Registers</li><li>Risk Response and Communication</li><li>Cost &amp; Schedule Risk Analysis (Monte Carlo)</li><li>Risk Management Training</li></ul>
  </section>

  <section class="abs service" style="top:825px">
    <svg class="icon" viewBox="0 0 40 40"><circle cx="20" cy="20" r="19" fill="#0a4fa3"/><rect x="13" y="10" width="14" height="20" rx="1.5" fill="none" stroke="#fff" stroke-width="1.6"/><rect x="15.5" y="12.5" width="9" height="4" fill="#fff"/><g fill="#fff"><rect x="15.5" y="19" width="2.5" height="2.5"/><rect x="19" y="19" width="2.5" height="2.5"/><rect x="22.5" y="19" width="2.5" height="2.5"/><rect x="15.5" y="23" width="2.5" height="2.5"/><rect x="19" y="23" width="2.5" height="2.5"/><rect x="22.5" y="23" width="2.5" height="2.5"/></g></svg>
    <h3>Cost Control:</h3>
    <ul><li>Estimating &amp; Forecasting</li><li>Earned Value Management</li><li>Progress Reporting</li><li>Cost Risk Analysis (Monte Carlo)</li></ul>
  </section>

  <div class="abs sky-bar"></div>

  <div class="abs contact" style="top:960px">
    <svg viewBox="0 0 28 28"><circle cx="14" cy="14" r="13.5" fill="#0a4fa3"/><path d="M10 8c1-.6 1.8-.4 2.3.5l1 2c.3.7.1 1.3-.5 1.7l-.8.5c.6 1.6 1.7 2.8 3.2 3.5l.6-.8c.4-.6 1-.7 1.7-.4l2 1c.9.5 1 1.3.5 2.2-1.2 1.8-3.1 1.8-5.4.4-2.6-1.6-4.4-4-5-6.7-.4-1.7 0-3.1.4-3.9z" fill="#fff"/></svg>
    <span>+353 (0)871 456 720</span>
  </div>
  <div class="abs contact" style="top:998px">
    <svg viewBox="0 0 28 28"><circle cx="14" cy="14" r="13.5" fill="#0a4fa3"/><rect x="8" y="9.5" width="12" height="9" rx="1" fill="none" stroke="#fff" stroke-width="1.5"/><path d="M8 10l6 5 6-5" fill="none" stroke="#fff" stroke-width="1.5"/></svg>
    <span>info@brackenservices.ie</span>
  </div>
  <div class="abs contact" style="top:1036px">
    <svg viewBox="0 0 28 28"><circle cx="14" cy="14" r="13.5" fill="#0a4fa3"/><g fill="none" stroke="#fff" stroke-width="1.3"><circle cx="14" cy="14" r="7"/><ellipse cx="14" cy="14" rx="3" ry="7"/><line x1="7" y1="14" x2="21" y2="14"/></g></svg>
    <span>www.brackenservices.ie</span>
  </div>
</div>
</body>
</html>
```